Briar Ridge Target Range wordpress theme

I want a Wordpress theme that is classy, unusual, colorful, etc. based on my attached logo files.

Font:
- Serpentine-Bold-Bold for "BRIAR RIDGE"
- BrowalliaUPC for "TARGET RANGE"

Colors (CMYK code):
- BLACK ....... 0; 0; 0; 100;
- ORANGE ... gradient from 0; 65; 97.5; 0 to 0; 39; 97.5; 0

```html
<!DOCTYPE html>
<html lang="en">
<head>
<meta charset="utf-8">
<title>Briar Ridge Target Range</title>
<link rel="stylesheet" href="https://fonts.googleapis.com/css2?family=Arimo:wght@400;700&family=Open+Sans:wght@400;600&family=Russo+One&family=Cinzel:wght@700&display=swap">
<style>
:root{
  --dark:#2d2d2d;
  --dark-2:#262626;
  --orange-1:#f2761b;
  --orange-2:#f9a33a;
  --orange-text:#ea7a1a;
  --light:#efefef;
  --text:#3c3c3c;
  --muted:#bdbdbd;
  --frame:#f4ead6;
}
*{box-sizing:border-box;margin:0;padding:0}
html,body{width:842px;height:1200px;overflow:hidden}
body{position:relative;background:var(--light);font-family:"Arimo",Arial,sans-serif;color:var(--text)}
.abs{position:absolute}
.top-band{left:0;top:0;width:842px;height:392px;background:linear-gradient(#343434,var(--dark-2))}
.footer{left:0;top:1010px;width:842px;height:190px;background:linear-gradient(#303030,var(--dark-2));border-top:2px solid #1d1d1d}

.brand{left:78px;top:16px;width:136px;text-align:center;font-weight:700;font-size:15px;line-height:18px;color:var(--orange-2);z-index:2}
.brand .dot{display:block;width:34px;height:34px;margin:0 auto 6px;border-radius:50%;background:var(--orange-1)}

.callout{right:71px;top:6px;text-align:right;font-family:"Open Sans",sans-serif}
.callout .label{color:var(--orange-2);font-size:13px}
.callout .num{color:#c9c9c9;font-size:20px;letter-spacing:.5px;line-height:22px}
.phone-icon{left:601px;top:12px;width:27px;height:27px;border-radius:5px;background:#111}
.follow{left:528px;top:68px;font-family:"Cinzel",serif;font-size:12px;color:#ddd;letter-spacing:1px}
.social{top:64px;width:22px;height:22px;border-radius:50%;background:#555}

.nav{left:76px;top:102px;width:694px;height:37px;border-radius:6px;background:linear-gradient(var(--orange-2),var(--orange-1));display:flex;align-items:center;padding-left:240px}
.nav a{display:block;flex:none;white-space:nowrap;text-align:center;color:#fff;text-decoration:none;font-size:10px;height:37px;line-height:37px;border-left:1px solid rgba(255,255,255,.35)}
.nav a:first-child{border-left:none}
.nav a.active{background:#262626;height:27px;line-height:27px;border-radius:3px;margin-right:9px}

.hero-frame{left:82px;top:163px;width:678px;height:297px;background:var(--frame);box-shadow:0 10px 16px rgba(0,0,0,.25)}
.hero-photo{left:88px;top:170px;width:665px;height:284px;background:radial-gradient(ellipse at 50% 40%,#b78452,#6b4526 70%,#3d2616)}
.shells{width:70px;height:75px;border-radius:14px;background:linear-gradient(135deg,#c5b280,#8b7a55);opacity:.85}

.intro-title{left:0;width:842px;top:505px;text-align:center;font-size:18px;color:#333}
.intro-title .mark{display:inline-block;width:18px;height:18px;border-radius:50%;background:var(--orange-1);vertical-align:-2px;margin-right:10px}
.intro-title b{font-family:"Russo One",sans-serif;font-weight:400;color:var(--orange-text);font-size:20px;letter-spacing:1px}
.intro{left:98px;width:670px;text-align:center;font-size:11px;line-height:17px;letter-spacing:.4px;color:#555}
.intro strong{color:#333}

.btn-wrap{left:296px;top:666px;width:214px;height:55px;border-radius:6px;background:linear-gradient(#e8e8e8,#c9c9c9);border:1px solid #bbb}
.btn{left:304px;top:675px;width:198px;height:37px;border-radius:3px;background:linear-gradient(var(--orange-2),#e2650d);color:#6e3407;font-weight:700;font-size:21px;letter-spacing:1px;text-align:center;line-height:37px}

.rule{left:80px;width:700px;height:2px;background:linear-gradient(90deg,transparent,#d2d2d2,transparent)}
.vrule{top:780px;width:1px;height:150px;background:#d8d8d8}
.feature{width:230px;text-align:center}
.feature .art{margin:0 auto;height:110px;border-radius:6px}
.feature h3{margin-top:17px;font-size:11px;color:var(--orange-text);letter-spacing:.5px}
.feature p{margin-top:4px;font-size:10px;line-height:14px;color:#555;letter-spacing:.3px}
.feature a{font-size:11px;font-weight:700;color:#333;text-decoration:none;letter-spacing:.5px}

.foot-brand{left:108px;top:1060px;width:104px;text-align:center;font-weight:700;font-size:13px;line-height:16px;color:var(--orange-2)}
.foot-brand .dot{display:block;width:30px;height:30px;margin:0 auto 6px;border-radius:50%;background:var(--orange-1)}
.copy{left:70px;top:1144px;width:180px;text-align:center;font-family:"Open Sans",sans-serif;font-size:9px;line-height:14px;color:var(--muted)}
.foot-text{font-family:"Open Sans",sans-serif;font-size:10px;line-height:20px;color:var(--muted);white-space:nowrap}
.map{left:282px;top:1082px;width:215px;height:103px;background:linear-gradient(135deg,#cfcbbf,#b9b6ac);border:3px solid #ddd}
.contact-h{left:565px;top:1037px;font-family:"Open Sans",sans-serif;font-size:12px;color:#aaa}
.contact-h b{font-weight:600;color:#ccc}
.contact-line{left:560px;top:1062px;width:200px;height:1px;background:#444}
.foot-phone{left:604px;top:1073px;font-family:"Open Sans",sans-serif;font-size:15px;color:#ddd}
.foot-mail{left:592px;top:1104px;font-family:"Open Sans",sans-serif;font-size:10px;color:#ccc}
.foot-social{top:1144px;width:18px;height:18px;border-radius:50%;background:#6a6a6a}
.blog{left:562px;top:1168px;font-family:"Open Sans",sans-serif;font-size:10px;color:#aaa}
</style>
</head>
<body>
<div class="abs top-band"></div>

<svg class="abs phone-icon" viewBox="0 0 27 27"><path d="M10 6c2 0 3 3 2 4l-1 1c1 2 2 4 4 5l1-1c1-1 4 0 4 2 0 1-1 3-3 3-5 0-10-5-10-10 0-2 2-4 3-4z" fill="#fff"/></svg>
<div class="abs callout"><div class="label">24/7 Call Out:</div><div class="num">(03) 55510482</div></div>
<div class="abs follow">Follow Us On</div>
<div class="abs social" style="left:640px"></div>
<div class="abs social" style="left:673px"></div>
<div class="abs social" style="left:707px"></div>
<div class="abs social" style="left:740px"></div>

<nav class="abs nav">
  <a class="active" href="#" style="width:59px">Home</a>
  <a href="#" style="width:104px">Services &amp; FAQ</a>
  <a href="#" style="width:96px">Membership</a>
  <a href="#" style="width:112px">Classes &amp; Events</a>
  <a href="#" style="width:74px">Contact</a>
</nav>

<div class="abs brand"><span class="dot"></span>Briar Ridge<br>Target Range</div>

<div class="abs hero-frame"></div>
<div class="abs hero-photo" role="img" aria-label="Indoor shooting range with ear protection, safety glasses and a pistol on the bench"></div>

<div class="abs shells" style="left:18px;top:470px" role="img" aria-label="Brass cartridges"></div>
<div class="abs shells" style="left:760px;top:455px" role="img" aria-label="Brass cartridges"></div>

<div class="abs intro-title"><span class="mark"></span><b>Briar Ridge</b> Target Range</div>
<p class="abs intro" style="top:550px"><strong>Ipsum is simply dummy text of the printing and typesetting industry. Lorem Ipsum has been the industry's standard</strong> dummy text ever since the 1500s, when an unknown printer took a galley of type and scrambled it to make a type specimen book. It has survived not only five centuries, but also the leap into electronic typesetting, remaining essentially unchanged.</p>
<p class="abs intro" style="top:617px">Ipsum is simply dummy text of the printing and typesetting industry. Lorem Ipsum has been the industry's standard dummy text ever since the 1500s, when an unknown printer took a galley of type and scrambled it to make a type.</p>

<div class="abs btn-wrap"></div>
<div class="abs btn">Learn More</div>

<div class="abs rule" style="top:744px"></div>
<div class="abs vrule" style="left:274px"></div>
<div class="abs vrule" style="left:532px"></div>

<div class="abs feature" style="left:40px;top:765px">
  <div class="art" style="width:130px;background:linear-gradient(135deg,#cfcfcf,#8a6a4a)" role="img" aria-label="Silver pistol beside a cigar"></div>
  <h3>Ipsum is simply dummy text</h3>
  <p>of the printing and typesetting<br>industry.Ipsum is simply</p>
  <a href="#">More Info</a>
</div>
<div class="abs feature" style="left:278px;top:765px">
  <div class="art" style="width:110px;background:linear-gradient(#d8c49c,#a88c60)" role="img" aria-label="Stack of paper silhouette targets"></div>
  <h3>Ipsum is simply dummy text</h3>
  <p>of the printing and typesetting<br>industry.Ipsum is simply</p>
  <a href="#">More Info</a>
</div>
<div class="abs feature" style="left:547px;top:765px">
  <div class="art" style="width:150px;background:linear-gradient(135deg,#e6e9f2,#3a3a3a)" role="img" aria-label="Pistol with trigger lock on a concealed carry certificate"></div>
  <h3>Ipsum is simply dummy text</h3>
  <p>of the printing and typesetting<br>industry.Ipsum is simply</p>
  <a href="#">More Info</a>
</div>

<div class="abs rule" style="top:970px"></div>

<footer class="abs footer"></footer>
<div class="abs foot-brand"><span class="dot"></span>Briar Ridge Target Range</div>
<div class="abs copy">© 2012 briarridgerange.example<br>All Rights Reserved</div>

<div class="abs foot-text" style="left:290px;top:1032px">1480 Briar Lane<br>Millbrook, TN 38000</div>
<div class="abs" style="left:385px;top:1034px;width:1px;height:36px;background:#555"></div>
<div class="abs foot-text" style="left:396px;top:1032px">Mon - Sat 9am - 8pm<br>Sunday 11am - 6pm</div>
<div class="abs map" role="img" aria-label="Street map showing the range location"></div>

<div class="abs contact-h"><b>Contact</b> Briar Ridge Target Range</div>
<div class="abs contact-line"></div>
<svg class="abs" style="left:572px;top:1076px" width="20" height="16" viewBox="0 0 20 16"><path d="M2 6c0-3 16-3 16 0v2h-4V6H6v2H2z M5 9h10l2 6H3z" fill="var(--orange-1)"/></svg>
<div class="abs foot-phone">555 - 018 - 2274</div>
<svg class="abs" style="left:566px;top:1104px" width="18" height="12" viewBox="0 0 18 12"><rect x="0.5" y="0.5" width="17" height="11" fill="none" stroke="var(--orange-1)"/><path d="M1 1l8 6 8-6" fill="none" stroke="var(--orange-1)"/></svg>
<div class="abs foot-mail">info@briarridgerange.example</div>
<div class="abs foot-social" style="left:604px"></div>
<div class="abs foot-social" style="left:633px"></div>
<div class="abs foot-social" style="left:662px"></div>
<div class="abs blog">Briar Ridge Target Range Blog</div>
</body>
</html>
```